Flyer-Design für Initiativbewerbung
Zielgruppe
Wir sind ein Buchhaltungsbüro. Mit diesem Flyer möchten wir uns bei Steuerberater als freier Mitarbeiter bewerben als initiativ Bewerbung! Ich lade Bilder von mir selbst mit hoch um so noch persönlicher zu werden. Die Bilder können gerne bearbeitet werden und Ausschnitte gezogen werden. Es soll sehr persönlich rüber kommen
Aufgabenstellung
Flyer sollte Din A Lang sein als Endformat, also gerne auch mehrseitig und max. 20 g haben
Sie können auch Textpassagen duplizieren und auf eine Vorderseite etc machen.
Es soll persönlich wirken obwohl es ein Werbeversand. Anbei auch das Logo unserer Firma.
Ich bin auch offen das Logo in Schwarz weiß darzustellen um so vom Blau wegzukommen.
Ich lasse mich gerne überraschen.
Text
Initiativ Bewerbung freier Mitarbeiter für Ihre Kanzlei
Sehr geehrte Damen und Herren,
gerne bewerben wir uns als freier Mitarbeiter im Rahmen des

```html
<!DOCTYPE html>
<html lang="de">
<head>
<meta charset="utf-8">
<title>Zahlwerk GmbH – Flyer Initiativbewerbung</title>
<link href="https://fonts.googleapis.com/css2?family=Montserrat:wght@400;500;600&display=swap" rel="stylesheet">
<style>
  :root {
    --brand-blue: #3063a5;
    --paper: #ffffff;
    --ink: #1d1d1b;
    --backdrop: #ebebeb;
    --photo-light: #d9dde0;
    --photo-dark: #8a7a6a;
    --signature-tint: #f3f3f3;
  }
  * { margin: 0; padding: 0; box-sizing: border-box; }
  html, body {
    width: 712px; height: 1200px; overflow: hidden;
    background: var(--backdrop);
    font-family: "Montserrat", sans-serif;
    color: var(--ink);
  }
  .flyer-spread {
    position: absolute; top: 261px; left: 24px;
    display: flex; gap: 24px;
  }
  .panel {
    position: relative; width: 320px; height: 678px;
    overflow: hidden;
    box-shadow: 0 8px 18px rgba(0,0,0,0.18);
  }

  /* Front panel */
  .panel--front { background: var(--brand-blue); }
  .brand-lockup {
    position: absolute; top: 232px; left: 0; width: 100%;
    display: flex; flex-direction: column; align-items: center;
    color: var(--paper);
  }
  .brand-lockup__square {
    width: 60px; height: 60px; margin-bottom: 22px;
    background: var(--paper);
  }
  .brand-lockup__name {
    font-weight: 500; font-size: 24px; line-height: 1.2;
  }
  .contact-band {
    position: absolute; top: 512px; left: 0; width: 100%; height: 109px;
    background: var(--paper); text-align: center;
    padding-top: 14px; font-weight: 500; font-size: 14px; line-height: 19.5px;
  }
  .contact-band__company { font-weight: 600; font-size: 17px; line-height: 24px; }
  .contact-band__divider { color: var(--brand-blue); }

  /* Back panel */
  .panel--back { background: var(--paper); }
  .letter-title {
    position: absolute; top: 36px; left: 0; width: 100%;
    text-align: center; font-weight: 600; font-size: 19px; line-height: 31px;
  }
  .letter-text {
    position: absolute; left: 16px; right: 16px;
    text-align: center; font-weight: 500; font-size: 11px; line-height: 17.5px;
  }
  .letter-text--salutation { top: 120px; }
  .letter-text--intro { top: 155px; }
  .letter-text--experience { top: 364px; }
  .service-list { position: absolute; top: 251px; left: 0; width: 100%; list-style: none; }
  .service-list__item {
    height: 19px; margin-bottom: 6px;
    background: var(--brand-blue); color: var(--paper);
    text-align: center; font-weight: 500; font-size: 15px; line-height: 19px;
  }
  .portrait {
    position: absolute; left: 0; bottom: 0; width: 250px; height: 210px;
    background: linear-gradient(200deg, var(--paper) 0%, var(--paper) 30%, var(--photo-light) 60%, var(--photo-dark) 100%);
  }
  .closing {
    position: absolute; top: 469px; left: 160px; width: 150px;
    text-align: center; font-weight: 500; font-size: 11px;
  }
  .closing__signature {
    height: 46px; margin: 10px 0 12px;
    background: var(--signature-tint); border-radius: 4px;
  }
  .corner-badge {
    position: absolute; right: 0; bottom: 0; width: 70px; height: 69px;
    background: var(--brand-blue);
    display: flex; align-items: center; justify-content: center;
  }
  .corner-badge__square { width: 26px; height: 26px; background: var(--paper); }
</style>
</head>
<body>
  <main class="flyer-spread">
    <section class="panel panel--front">
      <div class="brand-lockup">
        <div class="brand-lockup__square"></div>
        <div class="brand-lockup__name">Zahlwerk GmbH</div>
      </div>
      <div class="contact-band">
        <div class="contact-band__company">Zahlwerk GmbH</div>
        <div>Lindenallee 12 <span class="contact-band__divider">|</span> 70173 Musterstadt</div>
        <div>Tel : 0000/12345678</div>
        <div>email: info@zahlwerk-beispiel.de</div>
      </div>
    </section>

    <section class="panel panel--back">
      <h1 class="letter-title">Initiativ Bewerbung freier<br>Mitarbeiter für Ihre Kanzlei</h1>
      <p class="letter-text letter-text--salutation">Sehr geehrte Damen und Herren,</p>
      <p class="letter-text letter-text--intro">gerne bewerben wir uns als freier Mitarbeiter im Rahmen des § 17 BOStB für Ihre Kanzlei.<br>Gerne übernehmen wir für Sie im Rahmen der freien Mitarbeiter:</p>
      <ul class="service-list">
        <li class="service-list__item">Finanzbuchhaltung</li>
        <li class="service-list__item">Lohnbuchhaltung (auch Baulohn)</li>
        <li class="service-list__item">Jahresabschluss</li>
        <li class="service-list__item">Steuererklärungen</li>
      </ul>
      <p class="letter-text letter-text--experience">Fachliche Erfahrungen bestehen seit über 20 Jahren.<br>Die Tätigkeit auf diversen branchenüblichen Abrechnungsprogrammen ist uns vertraut.</p>
      <div class="portrait" role="img" aria-label="Foto des Geschäftsführers im hellen Sakko am Schreibtisch"></div>
      <div class="closing">
        <p>Mit freundlichen Grüßen,</p>
        <div class="closing__signature" role="img" aria-label="Handschriftliche Unterschrift"></div>
        <p>Jonas Berger</p>
      </div>
      <div class="corner-badge"><div class="corner-badge__square"></div></div>
    </section>
  </main>
</body>
</html>
```